RW Frameworks Inc Business cards

We need business cards using our existing logo but slightly modified. Right now the logo says RW Framework Masonry. We want to keep the RW part of the design, but replace the Framework Masonry portion with "FRAMEWORKS". Please see the attached file.
Ideally this would be a blank template so we can add Different Names, titles, and phone numbers later.
On the one side we want only the logo and on the other side the detail. I'm attaching an example for you to see.
Please reach out with any other questions. Our address and other details will be given out once we find a design we like.

Target Market(s)

Construction Industry

```html
<!DOCTYPE html>
<html lang="en">
<head>
<meta charset="utf-8">
<title>RW Frameworks Inc – Business Cards</title>
<link href="https://fonts.googleapis.com/css2?family=Bebas+Neue&family=Open+Sans:wght@400;600&display=swap" rel="stylesheet">
<style>
  :root {
    --backdrop: #e4e4e4;
    --card-white: #ffffff;
    --concrete-light: #8a8a88;
    --concrete-dark: #6b6b69;
    --brand-blue: #2a6fbe;
    --ink-grey: #6e6e6e;
    --emboss-grey: #5a5a58;
    --rule-grey: #b5b5b5;
  }
  * { margin: 0; padding: 0; box-sizing: border-box; }
  html, body { width: 1200px; height: 900px; overflow: hidden; }
  body {
    background: var(--backdrop);
    position: relative;
    font-family: "Open Sans", sans-serif;
  }
  .card {
    position: absolute;
    width: 525px;
    height: 300px;
    border-radius: 22px;
    box-shadow: 0 6px 18px rgba(0,0,0,0.18);
    overflow: hidden;
  }
  /* Logo side */
  .card--logo {
    left: 610px;
    top: 110px;
  }
  .card--logo .concrete-surface {
    position: absolute;
    inset: 0;
    background: radial-gradient(ellipse at 40% 35%, var(--concrete-light), var(--concrete-dark));
  }
  .card--logo .brand-name {
    position: absolute;
    inset: 0;
    display: flex;
    align-items: center;
    justify-content: center;
    font-family: "Bebas Neue", sans-serif;
    font-size: 62px;
    letter-spacing: 6px;
    color: var(--emboss-grey);
  }
  /* Detail side */
  .card--detail {
    left: 65px;
    top: 450px;
    background: var(--card-white);
    display: flex;
    align-items: center;
  }
  .brand-block {
    width: 262px;
    display: flex;
    justify-content: center;
    align-items: center;
    gap: 10px;
  }
  .brand-block .brand-mark {
    width: 14px;
    height: 14px;
    background: var(--brand-blue);
  }
  .brand-block .brand-name {
    font-family: "Bebas Neue", sans-serif;
    font-size: 40px;
    letter-spacing: 3px;
    color: var(--brand-blue);
  }
  .divider {
    width: 1px;
    height: 190px;
    background: var(--rule-grey);
  }
  .details {
    padding-left: 30px;
  }
  .person-name {
    font-family: "Bebas Neue", sans-serif;
    font-size: 40px;
    line-height: 1;
    color: var(--ink-grey);
    letter-spacing: 1px;
  }
  .job-title {
    font-family: "Bebas Neue", sans-serif;
    font-size: 20px;
    color: var(--brand-blue);
    letter-spacing: 1px;
    margin-bottom: 18px;
  }
  .contact {
    list-style: none;
    font-size: 15px;
    color: var(--ink-grey);
  }
  .contact li {
    display: flex;
    align-items: center;
    gap: 10px;
    margin-bottom: 8px;
  }
  .contact svg { width: 15px; height: 15px; fill: var(--brand-blue); }
</style>
</head>
<body>
  <section class="card card--logo" aria-label="Business card logo side">
    <div class="concrete-surface" role="img" aria-label="Grey concrete texture surface"></div>
    <div class="brand-name">RW FRAMEWORKS</div>
  </section>

  <section class="card card--detail" aria-label="Business card detail side">
    <div class="brand-block">
      <span class="brand-mark"></span>
      <span class="brand-name">RW FRAMEWORKS</span>
    </div>
    <div class="divider"></div>
    <div class="details">
      <h1 class="person-name">YOUR NAME</h1>
      <p class="job-title">JOB TITLE</p>
      <ul class="contact">
        <li>
          <svg viewBox="0 0 24 24" aria-hidden="true"><path d="M6.6 10.8a15.1 15.1 0 0 0 6.6 6.6l2.2-2.2a1 1 0 0 1 1-.25 11.4 11.4 0 0 0 3.6.57 1 1 0 0 1 1 1V20a1 1 0 0 1-1 1A17 17 0 0 1 3 4a1 1 0 0 1 1-1h3.5a1 1 0 0 1 1 1c0 1.25.2 2.45.57 3.57a1 1 0 0 1-.25 1z"/></svg>
          <span>000 000 0000</span>
        </li>
        <li>
          <svg viewBox="0 0 24 24" aria-hidden="true"><path d="M2 5h20v14H2z M2 5l10 8 10-8" /></svg>
          <span>youremail@xyz.com</span>
        </li>
      </ul>
    </div>
  </section>
</body>
</html>
```